TPR Letterhead

We need a letterhead design that will be able to be used on all marketing products (letterhead, mail chimp, envelops, business cards, etc.) We are a law firm specializing primarily in transportation law but offer a wide range of services to our clients. We would like the design to be modern, simple, and professional. Our colors are black and gold, however, we've incorporated dark gray and white on other marketing products such as our website.

```html
<!DOCTYPE html>
<html lang="en">
<head>
<meta charset="utf-8">
<title>TPR Law Group Letterhead</title>
<link href="https://fonts.googleapis.com/css2?family=PT+Sans:wght@400;700&family=Libre+Baskerville:wght@400;700&display=swap" rel="stylesheet">
<style>
  :root {
    --bg: #e6e6e6;
    --paper: #ececed;
    --ink: #1b1b1b;
    --text: #5a5a5a;
    --gold: #a8916a;
    --stamp: #5b86d6;
    --footer: #3a3a3a;
  }
  * { margin: 0; padding: 0; box-sizing: border-box; }
  html, body { width: 1200px; height: 795px; overflow: hidden; background: var(--bg); }
  .canvas { position: relative; width: 1200px; height: 795px; }
  .letterhead {
    position: absolute; left: 331px; top: 20px; width: 538px; height: 755px;
    background: var(--paper);
    box-shadow: 0 2px 10px rgba(0,0,0,.12);
    font-family: "PT Sans", sans-serif;
  }
  .brand {
    position: absolute; left: 39px; top: 60px;
    display: flex; align-items: center; gap: 8px;
  }
  .brand-square { width: 12px; height: 12px; background: var(--gold); }
  .brand-name {
    font-family: "PT Sans", sans-serif; font-weight: 400;
    font-size: 19px; letter-spacing: 1.5px; color: var(--ink);
  }
  .letter-body {
    position: absolute; left: 61px; top: 210px; width: 418px;
    font-size: 9.4px; line-height: 14.7px; color: var(--text);
  }
  .letter-body p + p { margin-top: 14.7px; }
  .closing {
    position: absolute; left: 413px; top: 491px;
    font-size: 9.4px; color: var(--text);
  }
  .seal {
    position: absolute; left: 382px; top: 510px; width: 76px; height: 76px;
  }
  .signature {
    position: absolute; left: 400px; top: 520px; width: 70px; height: 34px;
    background: linear-gradient(90deg, rgba(30,30,30,.18), rgba(30,30,30,.06));
    border-radius: 3px;
  }
  .contact {
    position: absolute; top: 711px;
    font-family: "Libre Baskerville", serif; font-size: 7px; line-height: 12px;
    color: var(--footer);
  }
  .contact-line { display: flex; align-items: center; gap: 6px; }
  .contact-line svg { width: 8px; height: 8px; flex: none; }
  .contact-phone { left: 39px; }
  .contact-address { left: 192px; }
  .contact-web { left: 391px; }
  .contact-web b { font-weight: 700; }
  .indent { padding-left: 14px; }
  .gold-band {
    position: absolute; left: 0; bottom: 0; width: 100%; height: 7px; background: var(--gold);
  }
</style>
</head>
<body>
<div class="canvas">
  <article class="letterhead">
    <header class="brand">
      <span class="brand-square"></span>
      <span class="brand-name">TPR LAW GROUP</span>
    </header>

    <section class="letter-body">
      <p>Lorem ipsum dolor sit amet, consectetur adipiscing elit. Donec orci purus, luctus vitae dignissim eu, iaculis sed purus. Vivamus faucibus, ipsum nec aliquet viverra, leo mauris condimentum ligula, sit amet sagittis enim ligula quis arcu. Nam egestas tortor id nisi porttitor mattis. In tortor ante, ultricies in suscipit a, tempus non massa. Vivamus et auctor mi. Fusce vel massa nulla. Phasellus nec eros mauris, et scelerisque orci.</p>
      <p>Donec malesuada orci vitae nulla accumsan porta a id massa. Quisque accumsan iaculis magna sit amet fringilla. Maecenas consequat, magna eget tincidunt semper, odio nibh rutrum mi, id feugiat ante nisi eu risus. Vestibulum nunc orci, rhoncus a placerat in, ultricies in mi. Cras mattis varius eros, vel fringilla nisi suscipit eget. Quisque scelerisque sagittis nulla at porttitor.</p>
      <p>Sed id augue vitae urna euismod commodo aliquet a quam. Pellentesque arcu velit, cursus et malesuada ut, consequat et diam. Nullam erat sem, rhoncus id ullamcorper vitae, rhoncus et arcu. In ultricies ultricies nulla, ut rutrum nisi iaculis at. Donec eu magna a metus ornare faucibus. Fusce aliquet faucibus ultricies. Morbi semper, est id tincidunt gravida, sem arcu adipiscing lacus, ac bibendum nulla leo eu purus. Quisque nec diam sed risus consectetur a ccumsan quis quis nibh. Vestibulum id purus lorem.</p>
    </section>

    <div class="closing">Sincerily,</div>
    <svg class="seal" viewBox="0 0 76 76" aria-hidden="true">
      <circle cx="38" cy="38" r="35" fill="none" stroke="var(--stamp)" stroke-width="2"/>
      <circle cx="38" cy="38" r="24" fill="none" stroke="var(--stamp)" stroke-width="1"/>
    </svg>
    <div class="signature" role="img" aria-label="Handwritten signature of the attorney"></div>

    <footer>
      <div class="contact contact-phone">
        <div class="contact-line">
          <svg viewBox="0 0 10 10"><path d="M2 1l2 2-1 1.2c.6 1.3 1.5 2.2 2.8 2.8L7 6l2 2-1.3 1.3C4.5 9 1 5.5.7 2.3z" fill="var(--gold)"/></svg>
          <span>555.014.2290</span>
        </div>
        <div class="contact-line">
          <svg viewBox="0 0 10 10"><rect x=".5" y="2" width="9" height="6" fill="none" stroke="var(--gold)"/><path d="M.5 2L5 5.5 9.5 2" fill="none" stroke="var(--gold)"/></svg>
          <span>info@tprlaw.com</span>
        </div>
      </div>
      <div class="contact contact-address">
        <div class="contact-line">
          <svg viewBox="0 0 10 10"><path d="M5 .5a3 3 0 0 1 3 3C8 6 5 9.5 5 9.5S2 6 2 3.5a3 3 0 0 1 3-3z" fill="none" stroke="var(--gold)"/><circle cx="5" cy="3.5" r="1" fill="var(--gold)"/></svg>
          <span>420 Harbor Lane, Suite 310</span>
        </div>
        <div class="indent">Lakeview, FL 30000</div>
      </div>
      <div class="contact contact-web">
        <div class="contact-line">
          <svg viewBox="0 0 10 10"><circle cx="5" cy="5" r="4.3" fill="none" stroke="var(--gold)"/><path d="M.7 5h8.6M5 .7c-2 2.5-2 6.1 0 8.6M5 .7c2 2.5 2 6.1 0 8.6" fill="none" stroke="var(--gold)" stroke-width=".7"/></svg>
          <span>www.<b>TPRLAW</b>.com</span>
        </div>
      </div>
    </footer>

    <div class="gold-band"></div>
  </article>
</div>
</body>
</html>
```